Rising with Quiet Steps Book Cover

I need an eBook cover for my book
Title: Rising with Quiet Steps - Calm Your Habits, Shape Your Days
Subtitle: Leave Behind Restless Cycles and Welcome a Steady Path of Vigor and Contentment
Author: Marcus Pellington

This book is about learning the mechanisms behind weight loss and how to cultivate two qualities: discipline and consistency

Target Market(s)

Weight Loss, Mind Hack

Requirements
Nice to have
• I would like to see 2 images of the same woman standing back to back. The one on the left is overweight and sad and the one on the right is not overweight and smiling.

```html
<!DOCTYPE html>
<html lang="en">
<head>
<meta charset="utf-8">
<title>Rising with Quiet Steps — Book Cover</title>
<link rel="stylesheet" href="https://fonts.googleapis.com/css2?family=Playfair+Display:wght@400&family=Cormorant+Garamond:wght@700&display=swap">
<style>
  :root {
    --wall: #47454b;
    --floor-top: #acacad;
    --floor-bottom: #a2a2a3;
    --silver-light: #f6f6f6;
    --silver-dark: #bdbdbf;
    --text-light: #ececec;
    --rule: #a9a8ac;
    --author: #0d0d0d;
    --photo-top: #8a7a62;
    --photo-mid: #2a272b;
    --photo-low: #6e5e5a;
  }
  html, body {
    margin: 0;
    padding: 0;
    width: 800px;
    height: 1200px;
    overflow: hidden;
    background: var(--wall);
  }
  .cover {
    position: relative;
    width: 800px;
    height: 1200px;
    background: var(--wall);
    overflow: hidden;
  }
  .floor {
    position: absolute;
    left: 0;
    top: 1079px;
    width: 800px;
    height: 121px;
    background: linear-gradient(var(--floor-top), var(--floor-bottom));
  }
  .title {
    position: absolute;
    left: 0;
    top: 66px;
    width: 800px;
    margin: 0;
    text-align: center;
    font-family: "Playfair Display", serif;
    font-weight: 400;
    font-size: 89px;
    line-height: 89px;
    letter-spacing: 1px;
    text-transform: uppercase;
    background: linear-gradient(180deg, var(--silver-light) 0%, var(--silver-dark) 100%);
    -webkit-background-clip: text;
    background-clip: text;
    color: transparent;
  }
  .title-line { display: block; }
  .title-rule {
    position: absolute;
    left: 97px;
    top: 259px;
    width: 604px;
    height: 1px;
    background: var(--rule);
  }
  .tagline {
    position: absolute;
    left: 0;
    top: 264px;
    width: 800px;
    margin: 0;
    text-align: center;
    font-family: "Playfair Display", serif;
    font-weight: 400;
    font-size: 27px;
    line-height: 36px;
    letter-spacing: 0.3px;
    text-transform: uppercase;
    color: var(--text-light);
  }
  .subtitle {
    position: absolute;
    left: 0;
    top: 308px;
    width: 800px;
    margin: 0;
    text-align: center;
    font-family: "Playfair Display", serif;
    font-weight: 400;
    font-size: 15.5px;
    line-height: 26px;
    letter-spacing: 1.3px;
    text-transform: uppercase;
    color: var(--text-light);
  }
  .photo {
    position: absolute;
    top: 381px;
    height: 750px;
    border-radius: 90px 90px 24px 24px;
    background: linear-gradient(180deg, var(--photo-top) 0%, var(--photo-mid) 35%, var(--photo-mid) 68%, var(--photo-low) 100%);
  }
  .photo-left { left: 112px; width: 186px; }
  .photo-right { left: 500px; width: 194px; }
  .author {
    position: absolute;
    left: 0;
    top: 1093px;
    width: 800px;
    margin: 0;
    text-align: center;
    font-family: "Cormorant Garamond", serif;
    font-weight: 700;
    font-size: 32px;
    line-height: 39px;
    letter-spacing: 9px;
    text-transform: uppercase;
    color: var(--author);
  }
  .author-line { display: block; }
</style>
</head>
<body>
<main class="cover">
  <div class="floor"></div>

  <h1 class="title">
    <span class="title-line">Rising with</span>
    <span class="title-line">Quiet Steps</span>
  </h1>
  <div class="title-rule"></div>
  <p class="tagline">– Calm Your Habits, Shape Your Days</p>
  <p class="subtitle">Leave Behind Restless Cycles and Welcome<br>a Steady Path of Vigor and Contentment</p>

  <div class="photo photo-left" role="img" aria-label="Photo of a woman with curly blonde hair in a black lace dress and heels, standing in profile facing left"></div>
  <div class="photo photo-right" role="img" aria-label="Photo of the same woman with a fuller figure in a black lace dress and heels, standing in profile facing right"></div>

  <p class="author">
    <span class="author-line">Marcus</span>
    <span class="author-line">Pellington</span>
  </p>
</main>
</body>
</html>
```